Tidewell Cruises. Discover the Coral Coast If You Can

Hello,
I have a catamaran charter business in the Whitsunday Islands, Australia.
My business is called Tidewell Cruises and my catamaran is a Mariner 380 K4 and his name is Quiet Drifter. I have attached its logo but would like something for Tidewell Cruises.
I am looking for a website for my business.
I'm also after 1 logos (for Tidewell Cruises).
I would like to be able to edit the website if needed (putting photos into the gallery, post reviews) and I'll need a shopping cart and all the usual social media contacts.
I will also need a live availability calendar for people to look at to see if the dates they want are available. I will need to easily edit this.
It must also stand out. I can supply most of the picture and maybe some video.
There will only be about 7 pages -
Home - Pictures scrolling past
Price and Availability - Have to show a live calendar that people can click on to see if the dates they want are available.
Gallery - I will put up photos and comments from past charterers.
Contact - A form they fill out to ask questions
Testimonials & Reviews - People can submit photos and review. I will have to be able to easily edit them.
Bookings & Store - If they want to pay by card, or if they want to buy any merchandise and so it would need a shopping cart.
Misc Page - What to bring, What to expect, etc etc
At the moment I only have 1 catamaran that will be advertised but I may get another at a later date.
The site will need a chilled out feel as people will be coming to the Whitsundays to relax and sail around.
The font needs to be a friendly font if this is possible.
The photo I uploaded called Gull Sketch is the logo I want for Tidewell Cruises.
Hope this helps.
Does this sound do-able

Target Market(s)

20 - 60

Industry/Entity Type

Tourism

Coding

Coded - Design and coding required

Number of Pages Required

5+ page

Colors

Designer to choose colors to be used in the design.

Requirements
Must have
• Chilled out feel

```html
<!DOCTYPE html>
<html lang="en">
<head>
<meta charset="utf-8">
<title>Tidewell Cruises — Beautiful Whitsundays</title>
<link rel="stylesheet" href="https://fonts.googleapis.com/css2?family=Bebas+Neue&family=Lato:wght@400;700&family=Roboto:wght@400;500&display=swap">
<style>
  :root {
    --sea-light: #3dd3e4;
    --sea-mid: #1fb3dc;
    --sea-deep: #3d6ff0;
    --ink: #555a5e;
    --muted: #9a9a9a;
    --white: #ffffff;
    --teal: #2ac4c4;
    --ocean: #2092c9;
    --accent: #3a8ee6;
    --footer: #3d8fe6;
    --social-one: #34508f;
    --social-two: #55acee;
    --social-three: #dd4b39;
  }
  * { box-sizing: border-box; margin: 0; padding: 0; }
  html, body { width: 1152px; height: 1200px; overflow: hidden; background: var(--white); }
  body { position: relative; font-family: "Lato", sans-serif; color: var(--ink); }
  .display { font-family: "Bebas Neue", sans-serif; font-weight: 400; }

  .hero-bg { position: absolute; left: 0; top: 0; width: 1152px; height: 520px; }

  .site-nav { position: absolute; left: 0; top: 0; width: 1152px; height: 100px; }
  .brand { position: absolute; left: 192px; top: 40px; font-size: 23px; color: var(--white); letter-spacing: .3px; }
  .nav-link { position: absolute; top: 41px; font-family: "Roboto", sans-serif; font-weight: 500; font-size: 13.5px; color: var(--white); text-decoration: none; }
  .nav-book { position: absolute; left: 742px; top: 34px; width: 112px; height: 29px; border-radius: 15px; background: var(--white);
    color: var(--accent); font-family: "Roboto", sans-serif; font-weight: 500; font-size: 12.5px; text-align: center; line-height: 29px;
    box-shadow: 0 4px 10px rgba(0,60,120,.25); }
  .cart { position: absolute; left: 875px; top: 37px; font-size: 22px; color: var(--white); }
  .cart-count { position: absolute; left: 950px; top: 33px; width: 32px; height: 32px; border-radius: 50%; background: var(--white);
    color: var(--accent); font-size: 20px; text-align: center; line-height: 34px; }

  .hero-title { position: absolute; left: 0; top: 0; color: var(--white); }
  .hero-kicker { position: absolute; left: 240px; top: 130px; font-size: 64px; line-height: 1; }
  .hero-main { position: absolute; left: 236px; top: 172px; font-size: 168px; line-height: 1; letter-spacing: 1px; white-space: nowrap; }
  .hero-sub { position: absolute; left: 294px; top: 303px; font-size: 66px; line-height: 1; white-space: nowrap; }

  .intro { position: absolute; left: 192px; top: 506px; width: 360px; text-align: center; font-size: 14.4px; line-height: 25.6px; color: var(--ink); }
  .day-title { position: absolute; left: 197px; top: 652px; font-size: 24px; color: var(--ink); }

  .photo-grid { position: absolute; left: 197px; top: 702px; width: 358px; height: 336px; display: grid;
    grid-template-columns: repeat(3, 1fr); grid-template-rows: 114px 114px 108px; overflow: hidden; }
  .photo { width: 100%; height: 100%; }
  .p1 { background: linear-gradient(180deg, #7fb3e0 0%, #2f6fa6 55%, #8a6a55 100%); }
  .p2 { background: linear-gradient(180deg, #8fb6d8 0%, #7a8a58 55%, #c9b88a 100%); }
  .p3 { background: linear-gradient(160deg, #2c2f5c 0%, #3f3f78 60%, #4a3d8c 100%); }
  .p4 { background: linear-gradient(160deg, #22333a 0%, #7a5a44 55%, #3a2c24 100%); }
  .p5 { background: linear-gradient(180deg, #5f7f5a 0%, #3e6a48 50%, #2f6f8c 100%); }
  .p6 { background: linear-gradient(160deg, #4b7a80 0%, #5b8a8a 60%, #4f7560 100%); }
  .p7 { background: linear-gradient(160deg, #2a4b5c 0%, #3d6a78 60%, #2a4e58 100%); }
  .p8 { background: linear-gradient(180deg, #c9b27a 0%, #b89a62 60%, #d07a3a 100%); }
  .p9 { background: linear-gradient(180deg, #6fb5c8 0%, #3f8aa0 60%, #2f6a7c 100%); }

  .gallery-cta { position: absolute; left: 265px; top: 966px; width: 206px; height: 47px; border-radius: 24px;
    background: linear-gradient(90deg, #1de9b6 0%, #1bc3c3 45%, #2196d0 100%); color: var(--white);
    display: flex; align-items: center; gap: 14px; padding-left: 38px; font-size: 22px; }
  .gallery-cta .mark { width: 30px; height: 30px; border-radius: 50%; border: 3px solid var(--white); }

  .dates-title { position: absolute; left: 644px; top: 452px; font-size: 44px; color: var(--white); line-height: 1; }
  .calendar { position: absolute; left: 643px; top: 509px; width: 317px; height: 303px; background: var(--white);
    box-shadow: 0 1px 4px rgba(0,0,0,.08); font-family: "Roboto", sans-serif; color: var(--muted); }
  .cal-month { position: absolute; left: 0; top: 33px; width: 100%; text-align: center; font-size: 19px; letter-spacing: .5px; }
  .cal-grid { position: absolute; left: 30px; top: 58px; width: 262px; display: grid; grid-template-columns: repeat(5, 1fr);
    grid-auto-rows: 39.4px; text-align: center; }
  .cal-day-name { font-size: 12.5px; font-weight: 500; line-height: 24px; height: 24px; }
  .cal-date { font-size: 15px; font-weight: 500; display: flex; align-items: center; justify-content: center; }
  .cal-date.selected span { width: 30px; height: 30px; border-radius: 50%; background: var(--accent); color: var(--white); line-height: 30px; }

  .btn { position: absolute; color: var(--white); text-align: center; border-radius: 30px; box-shadow: 0 4px 10px rgba(0,0,0,.12); }
  .btn-booked { left: 643px; top: 851px; width: 317px; height: 53px; background: var(--teal); font-size: 26px; line-height: 56px; }
  .btn-book { left: 686px; top: 912px; width: 242px; height: 46px; background: var(--ocean); font-size: 30px; line-height: 49px; }

  .follow-title { position: absolute; left: 709px; top: 980px; width: 200px; text-align: center; font-size: 22px; color: var(--ink); }
  .social { position: absolute; top: 1021px; width: 56px; height: 56px; border-radius: 50%; color: var(--white);
    font-family: "Lato", sans-serif; font-weight: 700; font-size: 10px; text-align: center; line-height: 56px; }
  .social-one { left: 716px; background: var(--social-one); }
  .social-two { left: 778px; background: var(--social-two); }
  .social-three { left: 840px; background: var(--social-three); }

  .site-footer { position: absolute; left: 0; top: 1117px; width: 1152px; height: 83px; background: var(--footer); }
  .copyright { position: absolute; right: 192px; top: 41px; font-size: 13px; color: var(--white); }
</style>
</head>
<body>

<svg class="hero-bg" viewBox="0 0 1152 520" aria-hidden="true">
  <defs>
    <linearGradient id="seaGradient" x1="0" y1="0" x2="1" y2="0.45">
      <stop offset="0" stop-color="#17a9d9"/>
      <stop offset="0.45" stop-color="#3dd3e4"/>
      <stop offset="0.75" stop-color="#37a9e8"/>
      <stop offset="1" stop-color="#3d62ef"/>
    </linearGradient>
  </defs>
  <path d="M0 0 H1152 V395 C1100 450 1030 494 955 508 L640 512 C470 450 240 396 0 410 Z" fill="url(#seaGradient)"/>
</svg>

<header class="site-nav">
  <div class="brand display">Tidewell Cruises</div>
  <a class="nav-link" style="left:372px">Availability</a>
  <a class="nav-link" style="left:472px">About</a>
  <a class="nav-link" style="left:543px">Gallery</a>
  <a class="nav-link" style="left:620px">Pricing</a>
  <a class="nav-link" style="left:697px">Shop</a>
  <div class="nav-book">Book Us</div>
  <div class="cart display">In my cart</div>
  <div class="cart-count display">2</div>
</header>

<h1 class="hero-title display">
  <span class="hero-kicker">Beautiful</span>
  <span class="hero-main">Whitsundays</span>
  <span class="hero-sub">Onboard with Tidewell Cruises</span>
</h1>

<p class="intro">Het standaard stuk van Lorum Ipsum wat sinds de 16e eeuw wordt gebruikt is hieronder, voor wie er interesse in heeft, weergegeven. Secties 1.10.32 en 1.10.33 van “de Finibus Bonorum et Malorum” door Marcellin zijn ook</p>

<h2 class="day-title display">A day on the Quiet Drifter</h2>

<section class="photo-grid">
  <div class="photo p1" role="img" aria-label="Guests relaxing on the catamaran deck in a bay"></div>
  <div class="photo p2" role="img" aria-label="Resort buildings on a green hillside above the beach"></div>
  <div class="photo p3" role="img" aria-label="Purple beach sign at dusk"></div>
  <div class="photo p4" role="img" aria-label="Gull Sketch tattoo on an arm"></div>
  <div class="photo p5" role="img" aria-label="Fishing rods on the boat near a green island"></div>
  <div class="photo p6" role="img" aria-label="Pink bougainvillea flowers over the water"></div>
  <div class="photo p7" role="img" aria-label="Giant clam on the reef"></div>
  <div class="photo p8" role="img" aria-label="Clownfish in a sea anemone"></div>
  <div class="photo p9" role="img" aria-label="Coral reef underwater"></div>
</section>

<div class="gallery-cta display">View more on Snapgram <span class="mark"></span></div>

<h2 class="dates-title display">Available dates</h2>

<section class="calendar">
  <div class="cal-month">APRIL</div>
  <div class="cal-grid">
    <div class="cal-day-name">Mon</div><div class="cal-day-name">Tue</div><div class="cal-day-name">Wed</div><div class="cal-day-name">Thu</div><div class="cal-day-name">Fri</div>
    <div class="cal-date">2</div><div class="cal-date">3</div><div class="cal-date">4</div><div class="cal-date">5</div><div class="cal-date">6</div>
    <div class="cal-date">9</div><div class="cal-date">10</div><div class="cal-date">11</div><div class="cal-date">12</div><div class="cal-date">13</div>
    <div class="cal-date">16</div><div class="cal-date">17</div><div class="cal-date">18</div><div class="cal-date selected"><span>19</span></div><div class="cal-date">20</div>
    <div class="cal-date">23</div><div class="cal-date">24</div><div class="cal-date">25</div><div class="cal-date">26</div><div class="cal-date">27</div>
    <div class="cal-date">30</div>
  </div>
</section>

<div class="btn btn-booked display">Already booked? What to do next?</div>
<div class="btn btn-book display">Book us</div>

<h3 class="follow-title display">Follow us</h3>
<div class="social social-one">Friendly</div>
<div class="social social-two">Chirper</div>
<div class="social social-three">Globe+</div>

<footer class="site-footer">
  <div class="copyright display">All rights reserved 2018</div>
</footer>

</body>
</html>
```